Flyer To Solicit Donations for a Good Cause

Hi. I am running the distance of a marathon race to solicit donations for a charitable cause. I need a well designed flyer to help me solicit support from friends and others. The copy for the flyer is attached. There is a significant amount of written text so it will need to be laid out in a way that is easy to read but also mixes well with some good images and design appeal. I am open to creative ideas. I have also attached my photo and a photo of me shaking hands with Mayor Velidis of Delphi and president of the Concordant Aegean Fellowship. Also there are some photos of the areas. These photos don't have to be used except for the one of me shaking hands with the Mayor and a caption underneath it. Otherwise, I am open to other stock photos or graphics. Feel free to contact me if you have questions. Thank you !

Update: ONE SIDED FLYER

Requirements
Must have
• Photo of the Mayor and Dale with the caption identifying us; All of the copy/text.

```html
<!DOCTYPE html>
<html lang="en">
<head>
<meta charset="utf-8">
<title>A Special Journey For Your Specific Prayers</title>
<link rel="stylesheet" href="https://fonts.googleapis.com/css2?family=Oswald:wght@600;700&family=Lato:ital,wght@0,400;0,700;1,400;1,700;1,900&display=swap">
<style>
  :root {
    --blue: #2b63c4;
    --blue-dark: #1d4a9e;
    --ink: #222;
    --orange: #f2a24a;
    --panel: #e6e6e8;
    --paper: #ffffff;
    --swoosh: #eceef2;
  }
  * { margin: 0; padding: 0; box-sizing: border-box; }
  html, body { width: 888px; height: 1200px; overflow: hidden; background: var(--paper); }
  .flyer {
    position: relative; width: 888px; height: 1200px; overflow: hidden;
    background: linear-gradient(160deg, #fff 40%, var(--swoosh) 60%, #fff 75%);
    font-family: "Lato", Arial, sans-serif; color: var(--ink);
  }
  .hero-photo {
    position: absolute; left: 0; top: 0; width: 888px; height: 330px;
    background: linear-gradient(180deg, #9fb6cf 0%, #c8d3de 38%, #6f7f5a 58%, #a89a80 78%, #8a7a62 100%);
  }
  .title-banner { position: absolute; left: 0; top: 322px; width: 888px; height: 115px; }
  .title {
    position: absolute; left: 0; top: 330px; width: 888px; text-align: center;
    font-family: "Oswald", Impact, sans-serif; font-weight: 700; color: #fff;
    font-size: 32px; line-height: 42px; letter-spacing: 0.3px; text-transform: uppercase;
    text-shadow: 0 2px 3px rgba(0,0,0,.35);
  }
  .intro { position: absolute; top: 462px; font-size: 15.2px; line-height: 18.3px; text-align: justify; }
  .intro p + p { margin-top: 9px; }
  .intro--left { left: 24px; width: 402px; }
  .intro--right { left: 558px; width: 0; }
  .intro--right { left: 558px; }
  .intro--right { left: 558px; width: 300px; }
  .intro--right { left: 558px; }
  .intro-col-right { position: absolute; top: 462px; left: 558px; width: 0; }
  .site { font-weight: 700; font-style: italic; }
  .cta-bar { position: absolute; left: 0; top: 675px; width: 888px; height: 44px; }
  .cta-text {
    position: absolute; left: 24px; top: 686px; font-size: 15.5px; font-weight: 700;
    color: var(--orange); font-style: italic;
  }
  .steps {
    position: absolute; left: 22px; top: 742px; width: 481px; height: 370px;
    background: var(--panel); border-radius: 10px; padding: 10px 14px 0 12px;
    list-style: none; font-size: 15.2px; line-height: 18.3px;
  }
  .steps li { position: relative; padding-left: 20px; margin-bottom: 16px; text-align: left; }
  .steps li::before {
    counter-increment: step; content: counter(step);
    position: absolute; left: 0; top: 2px; width: 15px; height: 15px; border-radius: 50%;
    background: var(--blue-dark); color: #fff; font-size: 10px; font-weight: 700;
    line-height: 15px; text-align: center;
  }
  .steps { counter-reset: step; }
  .steps strong { font-weight: 700; }
  .handshake-photo {
    position: absolute; left: 523px; top: 775px; width: 365px; height: 240px;
    background: linear-gradient(180deg, #d8e2ea 0%, #bfcfdc 45%, #6e7a8c 70%, #5c4a3c 100%);
  }
  .caption {
    position: absolute; left: 526px; top: 1016px; width: 362px; height: 48px;
    background: var(--blue); color: #fff; font-style: italic; font-weight: 700;
    font-size: 14.5px; line-height: 18px; text-align: center; padding-top: 6px;
  }
  .footer-band { position: absolute; left: 0; top: 1118px; width: 888px; height: 82px; }
  .footer-text {
    position: absolute; left: 0; top: 1160px; width: 888px; text-align: center;
    color: #fff; font-style: italic; font-weight: 700; font-size: 18px;
  }
</style>
</head>
<body>
<main class="flyer">
  <div class="hero-photo" role="img" aria-label="Ruined columns of the ancient circular temple at Delphi under a blue sky with mountains and pines"></div>

  <svg class="title-banner" viewBox="0 0 888 115" aria-hidden="true">
    <polygon points="0,0 888,0 888,22 0,22" fill="var(--blue)"/>
    <polygon points="90,22 130,22 175,112 140,112" fill="#c9ced8"/>
    <polygon points="798,22 758,22 713,112 748,112" fill="#c9ced8"/>
    <polygon points="50,0 838,0 758,110 130,110" fill="var(--blue)"/>
  </svg>
  <h1 class="title">A Special Journey For Your Specific Prayers<br>&amp; For An Important Ancient Cause</h1>

  <div class="intro intro--left">
    <p>This coming April 2016 Dale Hartwell will make a special running journey of 26 miles through the ancient lands of Apollo and Athena at Delphi on Mt. Parnassus in Greece.</p>
    <p>Dale will adorn his running outfit with special cloth strips that will contain written prayers and petitions of people who will sponsor his journey by making a charitable donation to the Concordant Aegean Fellowship, an organization that preserves the land and the Delphic culture. <span class="site">www.concordant-aegean-fellowship.org</span></p>
  </div>
  <div class="intro" style="left:558px;width:305px;">
    <p>The concept is simple and very powerful: as Dale runs, your written prayer on a cloth strip will flow and emanate in the wind --- being blessed by the spirits of this ancient and magical land --- asking unto the wind that your prayer be answered. This type of prayer practice dates back to ancient times. The Tibetan culture commonly uses prayer flags with special mantras and symbols.</p>
  </div>

  <svg class="cta-bar" viewBox="0 0 888 44" aria-hidden="true">
    <polygon points="0,0 872,0 888,22 872,44 0,44" fill="var(--blue)"/>
  </svg>
  <p class="cta-text">Will you make a prayer for yourself or a loved and support a good cause? Here is how to get your prayer started:</p>

  <ol class="steps">
    <li>Decide what you want your prayer, petition or intention to be.</li>
    <li>Define your prayer, petition or intention by writing it down.</li>
    <li>Refine it is <strong>concise, clear &amp; specific.</strong> (18 words or less is ideal for each strip cloth).</li>
    <li>Contact Dale at dale@hartwellreeves.com and tell him how many prayer cloth strips you wish to obtain. Dale will then send you the cloth for you to write your prayer and send back to him or he will write out the prayer for you. Dale can also answer any questions you may have.</li>
    <li>A minimum donation of $50 for each prayer cloth is requested. Checks can be made to the “Hartwell Reeves Trust Account/Concordant Aegean Fellowship” and mail to Dale T. Hartwell, Hartwell Reeves PLC, 4180 Linden Avenue, Ste. 204 Oakridge, Virginia 23999 or though online payment instructions sent by email from Dale as requested.</li>
  </ol>

  <div class="handshake-photo" role="img" aria-label="Dale shaking hands with Mayor Velidis in an office in front of a painted wall map"></div>
  <p class="caption">Mayor Velidis of Delphi and president of the<br>Concordant Aegean Fellowship.</p>

  <svg class="footer-band" viewBox="0 0 888 82" aria-hidden="true">
    <polygon points="0,38 888,38 888,82 0,82" fill="var(--blue)"/>
    <polygon points="212,0 690,0 740,38 162,38" fill="#c9ced8"/>
    <polygon points="215,4 687,4 735,44 167,44" fill="var(--blue)"/>
  </svg>
  <p class="footer-text">Your Prayer Can Make A Difference For You &amp; For A Good Cause !</p>
</main>
</body>
</html>
```